Webpage

I am a professional genealogist. I need a webpage that is professional looking (using the logo I chose), I can add hyperlinks and photos to if and when I want.

```html
<!DOCTYPE html>
<html lang="en">
<head>
<meta charset="utf-8">
<title>Holloway Research Services</title>
<link href="https://fonts.googleapis.com/css2?family=Arimo:wght@400;700&family=Questrial&family=Roboto+Condensed:wght@400&family=Noto+Serif:ital@0;1&display=swap" rel="stylesheet">
<style>
:root{
  --teal:#16aec4;
  --green:#2f9471;
  --ink:#333;
  --body:#555;
  --footer:#4b4b4b;
  --footer-text:#c9c9c9;
  --white:#fff;
}
*{margin:0;padding:0;box-sizing:border-box}
html,body{width:960px;height:1200px;overflow:hidden}
body{position:relative;font-family:"Arimo",Arial,sans-serif;color:var(--body);background:#e9ebeb}
.backdrop{position:absolute;inset:0;background:linear-gradient(90deg,#b9c4c6 0%,#f1f3f3 12%,#f6f7f7 50%,#f1f3f3 88%,#b5c1c3 100%)}
.sheet{position:absolute;left:96px;top:0;width:768px;height:1013px;background:linear-gradient(180deg,rgba(245,246,246,.95),rgba(255,255,255,.9) 60%,rgba(255,255,255,.97))}
.abs{position:absolute}

/* header */
.brand{left:108px;top:40px;display:flex;align-items:center;gap:14px}
.brand-dot{width:62px;height:62px;border-radius:50%;background:#7cc9b0}
.brand-name{font-family:"Questrial",sans-serif;font-size:22px;color:var(--ink)}
.contact-head{left:684px;top:14px;width:172px;font-family:"Questrial",sans-serif;color:var(--ink);line-height:16px;font-style:normal;white-space:nowrap}
.contact-head .name{color:var(--teal);font-size:19px;line-height:22px}
.contact-head .role{color:var(--teal);font-size:14.5px;line-height:22px}
.contact-head .addr{font-size:13px}
.contact-head .big{font-size:15px;line-height:19px;margin-top:3px}

/* nav */
.nav{left:96px;top:141px;width:768px;height:38px;background:var(--teal);border-top:2px solid #d7eef2;display:flex;justify-content:center;align-items:center}
.nav a{font-family:"Questrial",sans-serif;color:var(--white);text-decoration:none;font-size:14px;padding:0 22px;border-left:1px solid rgba(255,255,255,.3)}
.nav a:first-child{border-left:none}

/* hero */
.hero{left:96px;top:181px;width:768px;height:286px;background:linear-gradient(135deg,#6d5a48 0%,#a99a88 30%,#d9d2c7 55%,#c7b8a6 75%,#8c7f73 100%)}
.hero-caption{left:96px;top:405px;width:768px;text-align:center;font-size:29px;color:var(--white);text-shadow:0 1px 3px rgba(0,0,0,.6)}
.dots{left:460px;top:447px;display:flex;gap:4px}
.dots span{width:10px;height:10px;border-radius:50%;background:var(--white)}
.dots span.on{background:var(--teal)}

/* welcome */
.welcome-title{left:96px;top:482px;width:768px;text-align:center;font-family:"Roboto Condensed",sans-serif;font-weight:400;font-size:34px;color:var(--teal)}
.welcome-sub{left:96px;top:518px;width:768px;text-align:center;font-size:17px;color:var(--ink)}
.book{left:108px;top:550px;width:212px;height:150px;background:linear-gradient(135deg,#e9e4dc,#b39a7d 60%,#5a4c40)}
.welcome-text{left:336px;top:570px;width:515px;font-size:12.5px;line-height:19.2px}
.welcome-text p+p{margin-top:19px}

/* services */
.h2{font-family:"Roboto Condensed",sans-serif;font-weight:400;font-size:28px;color:var(--green)}
.services-title{left:108px;top:729px}
.services-intro{left:108px;top:770px;width:475px;font-size:12.5px;line-height:19.5px}
.services-list{list-style:none;font-size:13.5px;color:var(--ink)}
.services-list li{position:relative;padding-left:12px;height:25.5px}
.services-list li::before{content:"";position:absolute;left:0;top:5px;width:7px;height:7px;border-radius:50%;background:var(--teal)}
.col-a{left:108px;top:836px}
.col-b{left:348px;top:836px}

/* testimonials */
.testi-title{left:621px;top:729px}
.testi{left:621px;top:774px;width:236px;font-family:"Noto Serif",serif;color:var(--ink)}
.testi-text{font-style:italic;font-size:12px;line-height:19.4px;letter-spacing:-.15px}
.testi-name{margin-top:10px;font-size:15px}
.testi-place{margin-top:2px;font-size:12px}

/* footer */
.footer{left:0;top:1013px;width:960px;height:187px;background:var(--footer);border-top:5px solid #d3dad9}
.f-title{left:108px;top:1035px;font-size:16px;font-weight:700;color:var(--white)}
.f-photo{left:108px;top:1070px;width:44px;height:44px;border:2px solid #ddd;background:linear-gradient(#b7b2aa,#7e7770)}
.f-name{left:163px;top:1072px;color:var(--white);font-size:14px}
.f-role{left:163px;top:1094px;color:var(--white);font-size:12px}
.f-line{display:flex;gap:8px;font-size:12.5px;color:var(--footer-text);line-height:18.5px}
.f-line svg{flex:none;margin-top:2px}
.f-addr{left:110px;top:1130px}
.f-phone{left:346px;top:1124px}
.f-mail{left:346px;top:1148px}
.social{left:760px;top:1037px;display:flex;gap:6px}
.social span{width:26px;height:26px;border-radius:50%;background:#8b8b8b}
.f-nav{right:109px;top:1104px;text-align:right;font-family:"Questrial",sans-serif;font-size:11.5px;color:var(--white);line-height:18px}
.f-nav a{color:var(--white);text-decoration:none}
.f-nav i{font-style:normal;margin:0 8px}
.copy{right:106px;top:1149px;text-align:right;font-size:11.5px;line-height:16px;color:var(--footer-text)}
</style>
</head>
<body>
<div class="backdrop abs" role="img" aria-label="Bare tree branches in dark teal framing the page on a pale sky"></div>
<div class="sheet"></div>

<header>
  <div class="brand abs"><span class="brand-dot"></span><span class="brand-name">Holloway Research Services</span></div>
  <address class="contact-head abs">
    <div class="name">Dana Holloway,</div>
    <div class="role">Professional Genealogist</div>
    <div class="addr">PO Box 48150<br>Denton, TX 76202-4815</div>
    <div class="big">Call: 555-214-0187</div>
    <div class="big">Email: dh@holloway.net</div>
  </address>
</header>

<nav class="nav abs">
  <a href="#">HOME</a><a href="#">ABOUT</a><a href="#">SERVICES</a><a href="#">PUBLICATIONS</a><a href="#">BLOG</a><a href="#">LINKS</a><a href="#">CONTACT</a>
</nav>

<section>
  <div class="hero abs" role="img" aria-label="An older woman and a young woman smiling at each other over flowers"></div>
  <div class="hero-caption abs">Maecenas ultrices eros eget justo ultricies</div>
  <div class="dots abs"><span class="on"></span><span></span><span></span></div>
</section>

<section>
  <h1 class="welcome-title abs">WELCOME</h1>
  <p class="welcome-sub abs">Maecenas ultrices eros eget justo ultricies</p>
  <div class="book abs" role="img" aria-label="An open family history book beside an old portrait photograph"></div>
  <div class="welcome-text abs">
    <p>Maecenas ultrices eros eget justo ultricies in mollis augue commodo. Nullam sem tortor, volutpat non eleifend ut, adipiscing in augue. Aliquam at eros magna.</p>
    <p>Etiam tempus est quis massa sagittis sit amet lobortis quam malesuada. In interdum blandit ornare. Vivamus malesuada arcu in tellus consectetur rhoncus. Lorem ipsum dolor sit amet, con-sectetur adipiscing elit. Pellentesque rhoncus magna in tellus luctus gravida. Donec nisl diam, imperdiet eu pulvinar eget, faucibus eu mi.</p>
  </div>
</section>

<section>
  <h2 class="h2 services-title abs">Our Services</h2>
  <p class="services-intro abs">Maecenas ultrices eros eget justo ultricies in mollis augue commodo. Nullam sem tortor, volutpat non eleifend ut, adipiscing in augue.</p>
  <ul class="services-list col-a abs"><li>Forensic Genealogy</li><li>Kinship Determination</li><li>Research Analysis and Consultation</li></ul>
  <ul class="services-list col-b abs"><li>Texas Researcher</li><li>Record Retrieval</li></ul>
</section>

<section>
  <h2 class="h2 testi-title abs">Clients Testimonials</h2>
  <div class="testi abs">
    <p class="testi-text">Lorem ipsum dolor sit amet, consectetur adipiscing elit. Ut sit amet metus ut lorem pharetra venenatis fermentum at nibh. Nulla aliquet diam eu turpis con-vallis sit amet malesuada mi ultrices. In in velit massa, vitae condimentum leo. Vivamus nulla sapien, bibendum eget malesuada eget, volutpat nec nisl.</p>
    <div class="testi-name">Sam Rivera</div>
    <div class="testi-place">Denver, USA</div>
  </div>
</section>

<footer>
  <div class="footer abs"></div>
  <div class="f-title abs">HOLLOWAY RESEARCH SERVICES</div>
  <div class="f-photo abs" role="img" aria-label="Portrait of the genealogist"></div>
  <div class="f-name abs">Dana Holloway,</div>
  <div class="f-role abs">Professional Genealogist</div>
  <div class="f-line f-addr abs">
    <svg width="11" height="14" viewBox="0 0 11 14"><path d="M5.5 0A5.5 5.5 0 0 0 0 5.5C0 9.5 5.5 14 5.5 14S11 9.5 11 5.5A5.5 5.5 0 0 0 5.5 0z" fill="#16aec4"/><circle cx="5.5" cy="5.5" r="2" fill="#4b4b4b"/></svg>
    <span>PO Box 48150<br>Denton, TX 76202-4815</span>
  </div>
  <div class="f-line f-phone abs">
    <svg width="10" height="15" viewBox="0 0 10 15"><rect width="10" height="15" rx="2" fill="#16aec4"/><rect x="2" y="2" width="6" height="9" fill="#4b4b4b"/><circle cx="5" cy="13" r="1" fill="#4b4b4b"/></svg>
    <span>555-214-0187</span>
  </div>
  <div class="f-line f-mail abs">
    <svg width="14" height="10" viewBox="0 0 14 10" style="margin-top:4px"><rect width="14" height="10" fill="#16aec4"/><path d="M0 0l7 5 7-5" fill="none" stroke="#4b4b4b" stroke-width="1.3"/></svg>
    <span>dh@holloway.net</span>
  </div>
  <div class="social abs"><span aria-label="Social link"></span><span aria-label="Social link"></span><span aria-label="Social link"></span></div>
  <div class="f-nav abs">
    <a href="#">HOME</a><i>|</i><a href="#">ABOUT</a><i>|</i><a href="#">SERVICES</a><i>|</i><a href="#">PUBLICATIONS</a><br>
    <a href="#">BLOG</a><i>|</i><a href="#">LINKS</a><i>|</i><a href="#">CONTACT</a>
  </div>
  <div class="copy abs">Copyright © 2014 Holloway Research Services.<br>All Rights Reserved.</div>
</footer>
</body>
</html>
```